Sightless Fellowship Hall of San Diego needs an ad/flyer for convention program

Established in 1949, the Sightless Fellowship Hall of San Diego's mission is to enrich the lives of blind and visually impaired adults by preparing them for a normal, active life in a society that is principally sighted by encouraging independence.

Located in Harwick Gardens in San Diego, California, we are a nonprofit that gives blind and visually impaired people in our community an opportunity to socialize and interact. We help members build skills, confidence, and self-esteem through our various social, recreational, and educational activities. We were founded partially by Heron Guild members and receive ongoing funding from them.

We need an 8 1/2 by 11 inch color ad in jpg format. We would like it to be editable. This will be the foundation of our rebranding. The ad will be in a meeting program of the California Herons (californiaherons.example) with the goal of highlighting some of our programs in order to solicit donations from individual Heron Guilds, preferably ongoing ones.

We would like the ad to be generic enough that we can use the ad for other events and as a flyer in the future. We want the ad/flyer to be classic but eye popping with color. We want the design to reflect a professional and lively organization that loves to serve our members. We don’t entirely love our logo, but it’s what we have for now. Our next task will be a new logo design.

We would like to highlight some of our programs for our members include bingo, blind waterskiing and surfing, cooking and ceramic classes, foreign language classes, self defense classes, yoga, and craft classes. Many of the crafts our members make are sold during fundraisers, and they include blankets, scarves, beaded animals, and more. See a sampling of pictures. We provide transportation to and from our Center, free lunch while at the Center, and food to take home. Many of these activities continue during the pandemic via online platforms. We are doing monthly home deliveries of food to our members.

We need donations to keep our programs going, and we have building repairs & maintenance that we need donations in order to complete. See attached document regarding donations. Please reach out if you have questions. Thank you.

Web address: sfhsd.example
Street address: The Sightless Fellowship Hall of San Diego, 2716 Merrow St San Diego, CA 92107
Email address: donation@sfhsd.example
To make a donation: https://sfhsd.example/donate-2/

Donors

NonProfit

Sans Serif

Must have
• Highlight programs and information on how to make a donation.
Nice to have
• Information on how much each dollar donated will go - see attachment
Should not have
• Unprofessional or sloppy details

```html
<!DOCTYPE html>
<html lang="en">
<head>
<meta charset="utf-8">
<title>Sightless Fellowship Hall of San Diego – Donor Flyer</title>
<link rel="stylesheet" href="https://fonts.googleapis.com/css2?family=Rubik:wght@500;700;800&family=Open+Sans:wght@400;600;700&display=swap">
<style>
  :root{
    --crimson:#b3103f;
    --ink:#1e1b1c;
    --cream:#fff6ea;
    --peach:#fbd7b4;
    --blush:#f7b8c9;
    --apricot:#fcc478;
    --ring-pink:#f6a7a3;
    --ring-gold:#fdcf72;
    --ring-teal:#52b3ae;
    --white:#ffffff;
  }
  *{margin:0;padding:0;box-sizing:border-box}
  html,body{width:1028px;height:1200px;overflow:hidden;background:var(--white)}
  .flyer{
    position:relative;width:1028px;height:1200px;overflow:hidden;
    font-family:"Open Sans",sans-serif;color:var(--ink);
    background:
      radial-gradient(ellipse 260px 380px at 0% 8%, rgba(252,190,110,.75), transparent 70%),
      radial-gradient(ellipse 200px 520px at 100% 45%, rgba(245,140,175,.55), transparent 70%),
      radial-gradient(ellipse 280px 360px at 0% 85%, rgba(245,135,170,.6), transparent 70%),
      radial-gradient(ellipse 300px 260px at 95% 95%, rgba(252,200,130,.55), transparent 70%),
      radial-gradient(ellipse 360px 200px at 70% 2%, rgba(248,180,200,.45), transparent 70%),
      var(--cream);
  }
  .intro{position:absolute;top:36px;left:0;right:0;text-align:center}
  .intro h1{font-family:"Rubik",sans-serif;font-weight:800;font-size:44px;color:var(--crimson);letter-spacing:-.5px;margin-bottom:16px}
  .intro p{font-size:15px;line-height:1.45;max-width:720px;margin:0 auto 14px}
  .intro strong{font-family:"Rubik",sans-serif;font-weight:700}
  .intro .tight{margin-bottom:0}

  .pre-covid{
    position:absolute;left:46px;top:412px;width:940px;height:290px;
    border:2px solid var(--crimson);border-radius:22px;padding:6px 40px 0;
  }
  .pre-covid legend{
    font-family:"Rubik",sans-serif;font-weight:800;font-size:40px;color:var(--crimson);
    padding:0 14px;margin:0 auto;letter-spacing:-.5px;
  }
  .tiers{display:grid;grid-template-columns:1fr 1fr;column-gap:40px;row-gap:14px}
  .tier h3{font-family:"Rubik",sans-serif;font-weight:700;font-size:20px;color:var(--crimson);margin-bottom:8px}
  .tier ul{list-style:none}
  .tier li{position:relative;padding-left:18px;font-size:12.5px;font-weight:600;line-height:1.4;margin-bottom:5px}
  .tier li svg{position:absolute;left:0;top:3px}

  .lunch{position:absolute;top:722px;left:0;right:0;text-align:center;font-family:"Rubik",sans-serif;font-weight:500;color:var(--crimson)}
  .lunch p{font-size:20px;line-height:1.3}
  .lunch hr{width:440px;margin:10px auto 10px;border:0;border-top:2px solid var(--crimson)}

  .gallery{position:absolute;top:860px;left:0;right:0;display:flex;justify-content:center;gap:28px}
  .crafts{width:160px;height:160px;border-radius:50%;display:flex;align-items:center;justify-content:center}
  .crafts span{display:block;width:130px;height:130px;border-radius:50%}
  .crafts.pink{border:12px solid var(--ring-pink)}
  .crafts.pink span{background:linear-gradient(160deg,#e9e6e4,#2e4fb0)}
  .crafts.gold{border:12px solid var(--ring-gold)}
  .crafts.gold span{background:linear-gradient(160deg,#9f7fb8,#e7a4c4 50%,#7ec6c9)}
  .crafts.teal{border:12px solid var(--ring-teal)}
  .crafts.teal span{background:linear-gradient(160deg,#ece8e4,#6e6c6c 60%,#2d2c2e)}

  .footer{
    position:absolute;left:0;right:0;bottom:0;height:136px;background:var(--white);
    border-top-right-radius:80px;display:flex;align-items:center;justify-content:space-between;padding:0 46px 0 34px;
  }
  .contact{width:230px;text-align:center;font-family:"Rubik",sans-serif;font-size:12px}
  .contact .address{font-weight:500;line-height:1.35;padding-bottom:8px;border-bottom:1px solid var(--ink);margin-bottom:10px;display:flex;gap:6px;justify-content:center}
  .contact .links{display:flex;gap:6px;justify-content:center;align-items:center;font-size:12.5px}
  .brand{font-family:"Rubik",sans-serif;font-weight:700;font-size:20px;color:var(--ink);text-align:center;line-height:1.15;display:flex;align-items:center;gap:10px}
  .brand i{display:block;width:14px;height:14px;border-radius:50%;background:var(--ink)}
  .donate{text-align:center;font-family:"Rubik",sans-serif}
  .donate .box{width:70px;height:46px;margin:0 auto 8px;border-radius:4px;background:linear-gradient(180deg,#f7a9a4,#ef8f8c)}
  .donate b{display:block;font-weight:700;font-size:13.5px}
  .donate span{font-size:13.5px}
</style>
</head>
<body>
<main class="flyer">
  <section class="intro">
    <h1>Did you know?</h1>
    <p>During the pandemic we offer Bingo, Trivia and other virtual games every week, where blind and low vision participants can win SFH bucks. <strong>You can sponsor one day of games for $35.</strong></p>
    <p>You can provide 75 gift bags for our ‘We are in This Together’ home delivery program. Many of our blind and low vision people are isolated and stuck at home. These gift packages are welcomed with enthusiasm and gratefulness. Your rewards are huge smiles and happy faces.</p>
    <p>Our building is over 20 years old and requires ongoing maintenance and repairs</p>
    <p><strong>Fencing (cage) required to protect outside air conditioning units from vandalism. Cost: $2,500</strong></p>
    <p class="tight">Wanted: Sponsors for weekly virtual bingo and trivia games: Blind and Low vision participants receive one SFH buck per win. SFH bucks are turned into gift cards and HTL transportation passes.<br><strong>Sponsor one week for $40. Sponsor 1 month for $160</strong></p>
  </section>

  <fieldset class="pre-covid">
    <legend>Pre-Covid:</legend>
    <div class="tiers">
      <div class="tier">
        <h3>$10 per month or $120 will buy:</h3>
        <ul>
          <li><svg width="11" height="11" viewBox="0 0 11 11"><circle cx="5.5" cy="5.5" r="4.6" fill="none" stroke="#b3103f"/><path d="M3.3 5.7l1.6 1.5 2.8-3" fill="none" stroke="#b3103f"/></svg>60 meals for our lunch program – we serve<br>130 meals each week</li>
          <li><svg width="11" height="11" viewBox="0 0 11 11"><circle cx="5.5" cy="5.5" r="4.6" fill="none" stroke="#b3103f"/><path d="M3.3 5.7l1.6 1.5 2.8-3" fill="none" stroke="#b3103f"/></svg>13 round trip HTL transportation tickets</li>
          <li><svg width="11" height="11" viewBox="0 0 11 11"><circle cx="5.5" cy="5.5" r="4.6" fill="none" stroke="#b3103f"/><path d="M3.3 5.7l1.6 1.5 2.8-3" fill="none" stroke="#b3103f"/></svg>Enough beads to make 35 Rosa Lee angels in our craft class</li>
        </ul>
      </div>
      <div class="tier">
        <h3>$50 per month or $600 will buy:</h3>
        <ul>
          <li><svg width="11" height="11" viewBox="0 0 11 11"><circle cx="5.5" cy="5.5" r="4.6" fill="none" stroke="#b3103f"/><path d="M3.3 5.7l1.6 1.5 2.8-3" fill="none" stroke="#b3103f"/></svg>300 lunches</li>
          <li><svg width="11" height="11" viewBox="0 0 11 11"><circle cx="5.5" cy="5.5" r="4.6" fill="none" stroke="#b3103f"/><path d="M3.3 5.7l1.6 1.5 2.8-3" fill="none" stroke="#b3103f"/></svg>Thanksgiving dinner with all the fixings<br>for 80 to 100 guests</li>
        </ul>
      </div>
      <div class="tier">
        <h3>$20 per month or $240 will buy:</h3>
        <ul>
          <li><svg width="11" height="11" viewBox="0 0 11 11"><circle cx="5.5" cy="5.5" r="4.6" fill="none" stroke="#b3103f"/><path d="M3.3 5.7l1.6 1.5 2.8-3" fill="none" stroke="#b3103f"/></svg>26 round trip HTL transportation tickets</li>
          <li><svg width="11" height="11" viewBox="0 0 11 11"><circle cx="5.5" cy="5.5" r="4.6" fill="none" stroke="#b3103f"/><path d="M3.3 5.7l1.6 1.5 2.8-3" fill="none" stroke="#b3103f"/></svg>One month of large print and Braille translation<br>newsletter printing</li>
        </ul>
      </div>
      <div class="tier">
        <h3>$100 per month or $1200 will buy:</h3>
        <ul>
          <li><svg width="11" height="11" viewBox="0 0 11 11"><circle cx="5.5" cy="5.5" r="4.6" fill="none" stroke="#b3103f"/><path d="M3.3 5.7l1.6 1.5 2.8-3" fill="none" stroke="#b3103f"/></svg>Approximately 10 Bingo parties including<br>food and prizes</li>
        </ul>
      </div>
    </div>
  </fieldset>

  <section class="lunch">
    <p>$1,083 per month or $13,000 per year will fund our entire<br>lunch program for the year.</p>
    <hr>
    <p>Every dollar donated goes to support SFH participants<br>and programs.</p>
  </section>

  <section class="gallery">
    <div class="crafts pink"><span role="img" aria-label="Photo of a blue beaded angel ornament made in craft class"></span></div>
    <div class="crafts gold"><span role="img" aria-label="Photo of a stack of colourful handmade knitted blankets"></span></div>
    <div class="crafts teal"><span role="img" aria-label="Photo of a beaded penguin sitting on a knitted grey blanket"></span></div>
  </section>

  <footer class="footer">
    <div class="contact">
      <div class="address">
        <svg width="10" height="14" viewBox="0 0 10 14"><path d="M5 0a5 5 0 0 0-5 5c0 3.6 5 9 5 9s5-5.4 5-9a5 5 0 0 0-5-5zm0 7a2 2 0 1 1 0-4 2 2 0 0 1 0 4z" fill="#b3103f"/></svg>
        <span>The Sightless Fellowship Hall of San Diego,<br>2716 Merrow St San Diego, CA 92107</span>
      </div>
      <div class="links">
        <svg width="12" height="9" viewBox="0 0 12 9"><rect width="12" height="9" fill="#b3103f"/><path d="M0 0l6 5 6-5" fill="none" stroke="#fff"/></svg>
        <span>donation@sfhsd.example</span><span>|</span>
        <svg width="10" height="10" viewBox="0 0 10 10"><circle cx="5" cy="5" r="4.4" fill="none" stroke="#b3103f"/><path d="M.6 5h8.8M5 .6c-2.4 2.6-2.4 6.2 0 8.8M5 .6c2.4 2.6 2.4 6.2 0 8.8" fill="none" stroke="#b3103f" stroke-width=".8"/></svg>
        <span>sfhsd.example</span>
      </div>
    </div>
    <div class="brand"><i></i>Sightless Fellowship<br>Hall</div>
    <div class="donate">
      <div class="box" role="img" aria-label="Illustration of a pink donation box with leaves"></div>
      <b>To make a donation:</b>
      <span>https://sfhsd.example/donate-2/</span>
    </div>
  </footer>
</main>
</body>
</html>
```